Design Cover for Catalog and theme pages to match cover design for continuity

I need a catalog cover for our new catalog and have it flow through the pages uniting the design together. Most the hardest work is complete however it needs a designers touch to bring it all together. The attached files include the catalog with products images data and logos. We have more assets however with the 100MB limit we are unable to upload to many more. For additional images you can pull them from our website www.brandowave.example.

Target Market(s)

Tradesmen and trades women who work in the Electrical and Industrial Automation spaces.

Industry/Entity Type

Industrial

Font styles to use
Sans Serif

Colors
3176b5
0555a3
85cae6

Requirements
Must have
• Complete cover design
• Must also have cover theme flow through remaining pages
Nice to have
• Header and Footer on each page
• Index on cover with page reference
Should not have
• This is not a redesign of the whole catalog, please don't drastically change the pages or any of the data in the tables.

```html
<!DOCTYPE html>
<html lang="en">
<head>
<meta charset="utf-8">
<title>Brandowave Catalog – Cover and Page Theme</title>
<link rel="stylesheet" href="https://fonts.googleapis.com/css2?family=Titillium+Web:wght@400;600;700&family=Roboto:wght@400;500&display=swap">
<style>
  :root {
    --bg: #eceeef;
    --navy: #2b3592;
    --royal: #0555a3;
    --blue: #3176b5;
    --sky: #85cae6;
    --cyan: #27a6dc;
    --white: #ffffff;
    --paper: #f7f8f9;
    --ink: #1b1b1b;
    --rule: #c9ced6;
  }
  * { box-sizing: border-box; margin: 0; padding: 0; }
  html, body { width: 1200px; height: 848px; overflow: hidden; }
  body {
    background: var(--bg);
    font-family: "Titillium Web", "Roboto", sans-serif;
    color: var(--ink);
    position: relative;
  }

  /* Main cover */
  .cover {
    position: absolute;
    overflow: hidden;
    background: linear-gradient(180deg, #2f6fb8 0%, #2d4fa6 45%, var(--navy) 100%);
    box-shadow: 0 6px 18px rgba(0,0,0,.18);
  }
  .cover--main { left: 472px; top: 48px; width: 256px; height: 396px; }
  .cover__diecut {
    position: absolute; border-radius: 50%;
    background: radial-gradient(circle at 40% 35%, var(--sky) 0%, var(--cyan) 70%, #1d86c4 100%);
    box-shadow: inset 3px 4px 8px rgba(0,0,0,.35);
  }
  .cover--main .cover__diecut { left: 78px; top: 104px; width: 100px; height: 100px; }
  .cover__brand {
    position: absolute; left: 0; right: 0; text-align: center;
    color: var(--white); font-weight: 600; letter-spacing: .5px;
  }
  .cover--main .cover__brand { top: 312px; font-size: 22px; }
  .cover__tagline {
    position: absolute; left: 0; right: 0; text-align: center;
    color: var(--white); text-transform: uppercase; letter-spacing: 1.2px;
  }
  .cover--main .cover__tagline { top: 346px; font-size: 6.5px; }

  .callout {
    position: absolute; left: 200px; top: 243px;
    display: flex; align-items: center;
    font-family: "Roboto", sans-serif; font-size: 13px; color: var(--ink);
  }
  .callout__line { width: 200px; height: 1px; background: var(--ink); margin-left: 2px; }

  /* Page row */
  .page {
    position: absolute; top: 556px; height: 174px; width: 120px; overflow: hidden;
    box-shadow: 0 4px 10px rgba(0,0,0,.15);
  }
  .page--white { background: var(--paper); }
  .page--sky { background: var(--cyan); }
  .page--navy { background: var(--navy); }

  .cover--small { left: 408px; top: 556px; width: 123px; height: 172px; }
  .cover--small .cover__diecut { left: 36px; top: 46px; width: 50px; height: 50px; }
  .cover--small .cover__brand { top: 132px; font-size: 11px; }
  .cover--small .cover__tagline { top: 150px; font-size: 3.5px; }

  .inside__mark {
    position: absolute; left: 36px; top: 40px; width: 52px; height: 52px; border-radius: 50%;
    background: radial-gradient(circle at 40% 35%, #e6e8eb, #b9bec5);
  }
  .inside__title { position: absolute; left: 46px; top: 116px; font-size: 4.5px; font-weight: 700; color: var(--cyan); }
  .inside__text { position: absolute; left: 46px; top: 124px; width: 56px; font-size: 3.6px; line-height: 1.4; color: var(--blue); }

  .contents { position: absolute; left: 36px; top: 118px; width: 62px; color: var(--white); font-size: 3.6px; }
  .contents__title { font-weight: 700; margin-bottom: 2px; }
  .contents__row { display: flex; justify-content: space-between; border-bottom: .5px solid rgba(255,255,255,.5); line-height: 1.55; }

  .divider__shape {
    position: absolute; border-radius: 50%; background: var(--white);
  }
  .divider__title {
    position: absolute; left: 58px; top: 56px;
    font-size: 6px; font-weight: 700; line-height: 1.05; text-transform: uppercase;
  }
  .divider--navy .divider__title { color: var(--cyan); }
  .divider--sky .divider__title { color: var(--navy); }

  .spec__head { position: absolute; left: 10px; top: 8px; font-size: 3.6px; font-weight: 700; color: var(--cyan); }
  .spec__tab { position: absolute; right: 6px; top: 7px; width: 8px; height: 5px; background: var(--cyan); }
  .spec__photo { position: absolute; border-radius: 1px; background: linear-gradient(180deg, #e3e5e8, #a8adb4); }
  .spec__table { position: absolute; left: 10px; width: 100px; border-collapse: collapse; font-size: 3px; color: #555; }
  .spec__table th { background: var(--cyan); color: var(--white); font-weight: 500; text-align: left; padding: 0 1px; height: 4px; }
  .spec__table td { border-bottom: .5px solid var(--rule); height: 3.4px; }

  .caption {
    position: absolute; top: 756px;
    font-family: "Roboto", sans-serif; font-size: 13.5px; color: var(--ink);
    text-align: center; line-height: 1.3;
  }
</style>
</head>
<body>

  <section class="cover cover--main" aria-label="Catalog cover">
    <div class="cover__diecut"></div>
    <p class="cover__brand">Brandowave</p>
    <p class="cover__tagline">Efficiency through simplicity</p>
  </section>

  <p class="callout">This will be diecutted<span class="callout__line"></span></p>

  <!-- Inside cover + contents -->
  <article class="page page--white" style="left:140px">
    <div class="inside__mark"></div>
    <p class="inside__title">Welcome to Brandowave</p>
    <p class="inside__text">Quality enclosures and parts for every trade.</p>
  </article>
  <article class="page page--sky" style="left:260px">
    <div class="contents">
      <p class="contents__title">Contents</p>
      <p class="contents__row"><span>Aluminium Boxes</span><span>04</span></p>
      <p class="contents__row"><span>Plastic Boxes</span><span>12</span></p>
      <p class="contents__row"><span>Cable Glands</span><span>20</span></p>
      <p class="contents__row"><span>Terminals</span><span>28</span></p>
      <p class="contents__row"><span>Accessories</span><span>36</span></p>
    </div>
  </article>

  <!-- Small cover -->
  <section class="cover cover--small" aria-label="Catalog cover, small">
    <div class="cover__diecut"></div>
    <p class="cover__brand">Brandowave</p>
    <p class="cover__tagline">Efficiency through simplicity</p>
  </section>

  <!-- Section divider spread -->
  <article class="page page--navy" style="left:567px; width:112px; background:linear-gradient(90deg,#5060b4,var(--navy) 60%)"></article>
  <article class="page page--navy divider--navy" style="left:679px">
    <div class="divider__shape" style="left:-60px; top:90px; width:120px; height:120px"></div>
    <p class="divider__title">Aluminium<br>Project<br>Boxes</p>
  </article>

  <!-- Inside page + second divider -->
  <article class="page page--white" style="left:818px">
    <p class="spec__head">Aluminium Project Boxes</p>
    <span class="spec__tab"></span>
    <div class="spec__photo" role="img" aria-label="Product photo of aluminium enclosures" style="left:40px; top:16px; width:50px; height:22px"></div>
    <table class="spec__table" style="top:42px">
      <tr><th>Model</th><th>Size</th><th>Price</th></tr>
      <tr><td></td><td></td><td></td></tr><tr><td></td><td></td><td></td></tr>
      <tr><td></td><td></td><td></td></tr><tr><td></td><td></td><td></td></tr>
      <tr><td></td><td></td><td></td></tr><tr><td></td><td></td><td></td></tr>
    </table>
    <div class="spec__photo" role="img" aria-label="Product photo of diecast boxes" style="left:12px; top:100px; width:40px; height:20px"></div>
    <table class="spec__table" style="top:124px">
      <tr><th>Model</th><th>Size</th><th>Price</th></tr>
      <tr><td></td><td></td><td></td></tr><tr><td></td><td></td><td></td></tr>
      <tr><td></td><td></td><td></td></tr><tr><td></td><td></td><td></td></tr>
      <tr><td></td><td></td><td></td></tr>
    </table>
  </article>
  <article class="page page--sky divider--sky" style="left:938px">
    <div class="divider__shape" style="left:-60px; top:90px; width:120px; height:120px"></div>
    <p class="divider__title">Lorem<br>Ipsum<br>Dolor</p>
  </article>

  <p class="caption" style="left:150px">Inside cover</p>
  <p class="caption" style="left:264px">Contents page</p>
  <p class="caption" style="left:441px">Cover</p>
  <p class="caption" style="left:630px">Section dividers</p>
  <p class="caption" style="left:828px">Inside page<br>(Colours follow<br>divider)</p>
  <p class="caption" style="left:944px">Second divider</p>

</body>
</html>
```